Web Design Front Page Only for Organic Skincare

We have been in business for nearly 20 years. We are run by all females and sell anything from aromatherapy, skincare and pharmacy types products to health food shops and pharmacy. We are looking for an attractive and colourful but simple front web page design for our wholesale customers to look at. We want our customers to start using our website to find information rather than ringing us. So we want it to be attractive to our buyers who are young and funky.
Updates

To give you an idea of the products we sell to pharmacy and health food shops also beauty shops and hair salons.  We mainly deal with organic body and skincare, aromatherapy oils and body products, but also do some simple pharmacy products such as bandages and pill boxes, finger splits, walking frames and wheelchairs.  We are only looking for the front page of the website.  The back-end will be done in-house.  We currently do not have a logo designed so I am thinking that once we have done the website design we can build a logo from it.  I like bright colours and want something that is inviting to further discover that we do many different types of products.

Target Market(s)

young girls who are our retail buyers

Industry/Entity Type

Pharmacy

Requirements
Must have
• A section which says

Customer Log in
Should not have
• don't worry about too much writing or tabs. We will insert these later. Just come up with design image.

```html
<!DOCTYPE html>
<html lang="en">
<head>
<meta charset="utf-8">
<title>Organic Skincare – Home</title>
<link rel="stylesheet" href="https://fonts.googleapis.com/css2?family=Arimo:wght@400;700&family=PT+Sans:wght@400;700&display=swap">
<style>
:root{
  --lime:#b5cc1e;
  --lime-dark:#7f9a0c;
  --lime-light:#e6f25a;
  --olive:#6b8a0a;
  --yellow:#ffe61c;
  --yellow-soft:#fff48a;
  --orange:#f36f12;
  --text:#222;
  --line:#c9c9c9;
  --white:#fff;
  --price:#f26a10;
  --gold:#8a7a30;
}
*{box-sizing:border-box;margin:0;padding:0}
html,body{width:1029px;height:1200px;overflow:hidden;background:var(--white)}
body{position:relative;font-family:"Arimo",Arial,sans-serif;color:var(--text);font-size:14px}
.abs{position:absolute}

/* header */
.header{left:0;top:0;width:1029px;height:206px;
  background:radial-gradient(ellipse at 70% 20%,#e4f06a 0%,#b9d02a 40%,#93b011 100%)}
.header-photo{left:640px;top:0;width:300px;height:156px;
  background:radial-gradient(circle at 55% 40%,#f3e4d6 0%,#d9c2a8 35%,#c8dc6a 75%,rgba(185,208,42,0) 100%)}
.header-deco{left:0;top:0;width:160px;height:206px;
  background:linear-gradient(135deg,rgba(240,255,90,.55),rgba(240,255,90,0) 70%)}
.brand{left:104px;top:56px;font-family:"PT Sans",sans-serif;font-size:40px;line-height:44px;color:var(--white);letter-spacing:-.5px}
.tagline{left:108px;top:101px;font-size:13px;line-height:15px;color:var(--yellow)}
.nav{left:49px;top:156px;display:flex;gap:6px}
.nav a{width:182px;height:50px;border-radius:12px 12px 0 0;display:flex;align-items:center;justify-content:center;
  font-size:14px;font-weight:700;color:#1a1a1a;text-decoration:none;
  background:linear-gradient(#f4fb9c,#d3e640 55%,#b8cf1f)}
.nav a.active{background:linear-gradient(#ffb066,var(--orange) 60%,#e85e05)}
.nav-rule{left:0;top:206px;width:1029px;height:7px;background:var(--orange)}

/* utility bar */
.util{top:235px;font-size:13px;font-weight:700;color:#333;display:flex;align-items:center;gap:10px}
.flag{width:30px;height:19px;display:inline-block}
.select{border:1px solid #888;height:22px;width:158px;font-weight:400;font-size:14px;padding:2px 8px;position:relative;background:var(--white)}
.select::after{content:"";position:absolute;right:0;top:0;width:18px;height:20px;background:#ddd;border-left:1px solid #888}
.select svg{position:absolute;right:4px;top:7px;z-index:1}
.vsep{top:232px;width:1px;height:24px;background:var(--line)}
.cart-ico{width:26px;height:26px;border-radius:5px;background:linear-gradient(#c6e07a,#7fae2a);display:inline-flex;align-items:center;justify-content:center}

/* panels */
.panel{border:1px solid #d8d8d8;border-radius:8px;background:linear-gradient(90deg,#fff,#f1f1f1)}
.panel.yellow{border-color:#e2cc00;background:radial-gradient(ellipse at 80% 10%,var(--yellow-soft),var(--yellow) 60%)}
.panel.lime{border-color:#c9d82a;background:radial-gradient(ellipse at 80% 10%,#f7fca8,var(--lime-light) 60%)}
.panel h3{font-size:14px;font-weight:700;margin:22px 0 14px 22px}
.list{list-style:none;margin:0 20px 0 22px}
.list li{height:34px;border-bottom:1px dotted #aaa;display:flex;align-items:center;gap:8px;font-size:14px;color:#333;white-space:nowrap}
.list li:last-child{border-bottom:none}
.list svg{flex:none}

/* customer log in */
.login h3{margin:16px 0 10px 22px}
.field{margin-left:20px;width:178px;height:22px;border:1px solid #888;background:var(--white);font-size:12px;color:#888;padding:3px 7px}
.login-row{display:flex;gap:6px;margin:8px 0 0 20px}
.login-row .field{margin:0;width:110px}
.login-btn{width:62px;height:22px;border-radius:11px;background:linear-gradient(#dce86a,#a8c21a);color:var(--white);font-size:12px;display:flex;align-items:center;justify-content:center}

/* welcome */
.welcome{left:279px;top:273px;width:701px;height:174px;border:1px solid #c3d42a;border-radius:10px;
  background:linear-gradient(90deg,#d9ea4a 0%,#eef77a 40%,#f0f57c 60%,#cfe23a 100%);overflow:hidden}
.welcome-art{left:0;top:0;width:320px;height:174px;background:radial-gradient(circle at 50% 55%,#fbff9a,#d8ea40 55%,rgba(216,234,64,0))}
.welcome h1{left:334px;top:34px;font-family:"PT Sans",sans-serif;font-weight:400;font-size:29px;color:#5c7a08;letter-spacing:-.6px}
.welcome p{left:336px;top:82px;width:320px;font-size:14px;line-height:18px;color:#4a6306}

/* featured */
.featured{left:279px;top:461px;width:471px;height:641px;border:1px solid #d8d8d8;border-radius:8px;background:var(--white);overflow:hidden}
.featured-head{height:56px;background:linear-gradient(#f2f2f2,#d4d4d4);font-weight:700;font-size:16px;padding:20px 0 0 25px}
.product{position:absolute;left:0;width:471px;height:196px}
.product + .product::before{content:"";position:absolute;left:22px;right:24px;top:0;border-top:1px dotted #999}
.thumb{position:absolute;left:42px;top:24px;width:90px;height:76px;border-radius:6px}
.price{position:absolute;left:30px;top:124px;width:120px;text-align:center;font-family:"PT Sans",sans-serif;font-size:21px;color:var(--price)}
.pname{position:absolute;left:196px;top:22px;font-weight:700;font-size:14px;color:var(--olive)}
.pdesc{position:absolute;left:196px;top:50px;width:250px;font-size:14px;line-height:17px;color:#333}
.btn{position:absolute;left:196px;width:80px;height:26px;border-radius:13px;color:var(--white);font-size:13px;display:flex;align-items:center;justify-content:center}
.btn.details{top:96px;background:linear-gradient(#c9c9c9,#9a9a9a)}
.btn.cart{top:128px;width:113px;background:linear-gradient(#dce86a,#a8c21a)}

/* special */
.special-img{left:785px;top:784px;width:170px;height:193px;border:1px solid #bbb;background:var(--white);display:flex;align-items:center;justify-content:center}
.special-img span{width:120px;height:150px;border-radius:40% 40% 30% 30%;background:radial-gradient(circle at 45% 60%,#e8f07a,#9fb82a)}
.special-name{left:762px;top:993px;width:218px;text-align:center;font-size:14px}
.special-old{left:762px;top:1024px;width:218px;text-align:center;font-family:"PT Sans",sans-serif;font-size:20px;color:var(--gold);text-decoration:line-through}
.special-new{left:762px;top:1050px;width:218px;text-align:center;font-family:"PT Sans",sans-serif;font-size:22px;color:var(--gold)}

/* footer */
.footer{left:49px;top:1126px;width:931px;height:90px;border:1px solid #ddd;border-radius:8px}
.paybadge{top:1147px;height:26px;border:1px solid #666;display:flex;align-items:center;justify-content:center;font-size:11px;font-weight:700;color:#333;background:#eee;white-space:nowrap}
.flinks{left:277px;top:1146px;font-size:14px;color:var(--lime-dark)}
.copy{left:277px;top:1166px;font-size:11px;color:#222}
</style>
</head>
<body>

<header>
  <div class="abs header"></div>
  <div class="abs header-deco" role="img" aria-label="Yellow floral swirl ornament"></div>
  <div class="abs header-photo" role="img" aria-label="Photo of a young woman holding a white lily"></div>
  <div class="abs brand">Organic Skincare</div>
  <div class="abs tagline">the biggest online store</div>
  <nav class="abs nav">
    <a class="active" href="#">HOME PAGE</a>
    <a href="#">NEW PRODUCTS</a>
    <a href="#">SPECIALS</a>
    <a href="#">MY ACCOUNT</a>
    <a href="#">CONTACT US</a>
  </nav>
  <div class="abs nav-rule"></div>
</header>

<div class="abs util" style="left:86px">Choose your language:
  <span style="width:10px"></span>
  <svg class="flag" viewBox="0 0 30 19" role="img" aria-label="English"><rect width="30" height="19" fill="#23408e"/><path d="M0 0L30 19M30 0L0 19" stroke="#fff" stroke-width="4"/><path d="M15 0V19M0 9.5H30" stroke="#fff" stroke-width="6"/><path d="M15 0V19M0 9.5H30" stroke="#cf142b" stroke-width="3"/></svg>
  <svg class="flag" viewBox="0 0 30 19" role="img" aria-label="German"><rect width="30" height="6.3" fill="#000"/><rect y="6.3" width="30" height="6.4" fill="#dd0000"/><rect y="12.7" width="30" height="6.3" fill="#ffce00"/></svg>
</div>
<div class="abs vsep" style="left:361px"></div>
<div class="abs util" style="left:396px">Currencies:
  <div class="select">US Dollar<svg width="9" height="6" viewBox="0 0 9 6"><path d="M0 0H9L4.5 6Z" fill="#222"/></svg></div>
</div>
<div class="abs vsep" style="left:681px"></div>
<div class="abs util" style="left:719px">Shopping Cart:
  <span class="cart-ico"><svg width="16" height="14" viewBox="0 0 16 14"><path d="M1 1H3L5 9H13L15 3H4" fill="none" stroke="#fff" stroke-width="1.6"/><circle cx="6" cy="12" r="1.4" fill="#fff"/><circle cx="12" cy="12" r="1.4" fill="#fff"/></svg></span>
  <span style="margin-left:8px">5 items</span>
</div>

<aside>
  <section class="abs panel" style="left:49px;top:273px;width:218px;height:457px">
    <h3 style="margin-top:24px">Categories</h3>
    <ul class="list">
      <li><svg width="11" height="7" viewBox="0 0 11 7"><path d="M0 3.5H9M6 1L9.5 3.5L6 6" stroke="#333" fill="none"/></svg>Face Care</li>
      <li><svg width="11" height="7" viewBox="0 0 11 7"><path d="M0 3.5H9M6 1L9.5 3.5L6 6" stroke="#333" fill="none"/></svg>Body Care</li>
      <li><svg width="11" height="7" viewBox="0 0 11 7"><path d="M0 3.5H9M6 1L9.5 3.5L6 6" stroke="#333" fill="none"/></svg>Aromatherapy Oils</li>
      <li><svg width="11" height="7" viewBox="0 0 11 7"><path d="M0 3.5H9M6 1L9.5 3.5L6 6" stroke="#333" fill="none"/></svg>Hair Care</li>
      <li><svg width="11" height="7" viewBox="0 0 11 7"><path d="M0 3.5H9M6 1L9.5 3.5L6 6" stroke="#333" fill="none"/></svg>Bath and Shower</li>
      <li><svg width="11" height="7" viewBox="0 0 11 7"><path d="M0 3.5H9M6 1L9.5 3.5L6 6" stroke="#333" fill="none"/></svg>Baby Care</li>
      <li><svg width="11" height="7" viewBox="0 0 11 7"><path d="M0 3.5H9M6 1L9.5 3.5L6 6" stroke="#333" fill="none"/></svg>Men's Grooming</li>
      <li><svg width="11" height="7" viewBox="0 0 11 7"><path d="M0 3.5H9M6 1L9.5 3.5L6 6" stroke="#333" fill="none"/></svg>Natural Remedies</li>
      <li><svg width="11" height="7" viewBox="0 0 11 7"><path d="M0 3.5H9M6 1L9.5 3.5L6 6" stroke="#333" fill="none"/></svg>First Aid</li>
      <li><svg width="11" height="7" viewBox="0 0 11 7"><path d="M0 3.5H9M6 1L9.5 3.5L6 6" stroke="#333" fill="none"/></svg>Pill Boxes</li>
      <li><svg width="11" height="7" viewBox="0 0 11 7"><path d="M0 3.5H9M6 1L9.5 3.5L6 6" stroke="#333" fill="none"/></svg>Mobility Aids</li>
    </ul>
  </section>

  <section class="abs panel lime" style="left:49px;top:744px;width:218px;height:220px">
    <h3>Bestsellers</h3>
    <ul class="list">
      <li><svg width="11" height="7" viewBox="0 0 11 7"><path d="M0 3.5H9M6 1L9.5 3.5L6 6" stroke="#333" fill="none"/></svg>Essential Oil Sets</li>
      <li><svg width="11" height="7" viewBox="0 0 11 7"><path d="M0 3.5H9M6 1L9.5 3.5L6 6" stroke="#333" fill="none"/></svg>Organic Face Creams</li>
      <li><svg width="11" height="7" viewBox="0 0 11 7"><path d="M0 3.5H9M6 1L9.5 3.5L6 6" stroke="#333" fill="none"/></svg>Massage Oils</li>
      <li><svg width="11" height="7" viewBox="0 0 11 7"><path d="M0 3.5H9M6 1L9.5 3.5L6 6" stroke="#333" fill="none"/></svg>Hand and Foot Care</li>
    </ul>
  </section>

  <section class="abs panel login" style="left:49px;top:978px;width:218px;height:124px">
    <h3>Customer Log in</h3>
    <div class="field">Email address</div>
    <div class="login-row">
      <div class="field">Password</div>
      <div class="login-btn">log in</div>
    </div>
  </section>
</aside>

<section class="abs welcome">
  <div class="abs welcome-art" role="img" aria-label="Yellow lily flower illustration"></div>
  <h1 class="abs">Welcome to Organic Skincare</h1>
  <p class="abs">Nonummy hendreasells portausce varium sosatoque penatiusgnis dis parturientem ipsum dolor sit amonsectetuer.</p>
</section>

<section class="abs featured">
  <div class="featured-head">Featured products</div>
  <div class="product" style="top:56px">
    <div class="thumb" role="img" aria-label="Amber bottle of rosehip face oil" style="background:linear-gradient(135deg,#fff27a,#e8c400)"></div>
    <div class="price">$69.80</div>
    <div class="pname">Organic Rosehip Face Oil</div>
    <div class="pdesc">Proin dictum elementum velsce euis mod consequat antrem ipsum dolor.</div>
    <div class="btn details">details</div>
    <div class="btn cart">add to cart</div>
  </div>
  <div class="product" style="top:253px">
    <div class="thumb" role="img" aria-label="White jar of lavender body butter" style="background:linear-gradient(135deg,#f4f4f4,#c8c8c8)"></div>
    <div class="price">$45.40</div>
    <div class="pname">Lavender Body Butter</div>
    <div class="pdesc">Proin dictum elementum velsce euis mod consequat antrem ipsum dolor.</div>
    <div class="btn details">details</div>
    <div class="btn cart">add to cart</div>
  </div>
  <div class="product" style="top:448px">
    <div class="thumb" role="img" aria-label="Tube of aloe calming gel" style="background:linear-gradient(135deg,#eef4c0,#a8c060)"></div>
    <div class="price">$82.15</div>
    <div class="pname">Aloe Calming Gel</div>
    <div class="pdesc">Proin dictum elementum velsce euis mod consequat antrem ipsum dolor.</div>
    <div class="btn details">details</div>
    <div class="btn cart">add to cart</div>
  </div>
</section>

<section class="abs panel" style="left:762px;top:461px;width:218px;height:249px">
  <h3>Information</h3>
  <ul class="list">
    <li><svg width="11" height="7" viewBox="0 0 11 7"><path d="M0 3.5H9M6 1L9.5 3.5L6 6" stroke="#333" fill="none"/></svg>Shipping and returns</li>
    <li><svg width="11" height="7" viewBox="0 0 11 7"><path d="M0 3.5H9M6 1L9.5 3.5L6 6" stroke="#333" fill="none"/></svg>Privacy</li>
    <li><svg width="11" height="7" viewBox="0 0 11 7"><path d="M0 3.5H9M6 1L9.5 3.5L6 6" stroke="#333" fill="none"/></svg>Wholesale Terms</li>
    <li><svg width="11" height="7" viewBox="0 0 11 7"><path d="M0 3.5H9M6 1L9.5 3.5L6 6" stroke="#333" fill="none"/></svg>Gift Voucher FAQ</li>
    <li><svg width="11" height="7" viewBox="0 0 11 7"><path d="M0 3.5H9M6 1L9.5 3.5L6 6" stroke="#333" fill="none"/></svg>Product Catalogue</li>
  </ul>
</section>

<section class="abs panel yellow" style="left:762px;top:723px;width:218px;height:379px">
  <h3 style="margin-top:22px">Special</h3>
</section>
<div class="abs special-img"><span role="img" aria-label="Aromatherapy oil gift set"></span></div>
<div class="abs special-name">Aromatherapy Gift Set</div>
<div class="abs special-old">$95.10</div>
<div class="abs special-new">$84.25</div>

<footer>
  <div class="abs footer"></div>
  <div class="abs paybadge" style="left:75px;width:70px">PayNest</div>
  <div class="abs paybadge" style="left:147px;width:54px">CardOne</div>
  <div class="abs paybadge" style="left:203px;width:52px">DuoPay</div>
  <div class="abs flinks">Log In &nbsp;|&nbsp; My Account &nbsp;|&nbsp; Checkout</div>
  <div class="abs copy">Copyright © 2012 Organic Skincare Store &nbsp;|&nbsp; Privacy Policy &nbsp;|&nbsp; Terms Of Use</div>
</footer>

</body>
</html>
```